Packaging for Hair Fibers Product

We are a start up company looking for a new packaging design for hair building fibers. These are aimed at predominantly men but also women as well. We already have a logo and i have the packaging design from our competitors. We are wanting to keep the look masculine as 90% of our users will be middle aged men. We would like the colours to be black and white but are open to other colours as well.
It will need to have our logo and the following somewhere on the front.
"Instant Fuller & Thicker Hair" & "Natural Hair Building Fibers" "28g" or "Net Weight 28g"
We only need the front of the packaging designed, please make the other sides of the packaging the same colour but blank.
Target Market(s)
Men 25+
Industry/Entity Type
Hair And Beauty
Requirements
Must have
- Logo which i have included. and the following somewhere on the front.
- "Instant Fuller & Thicker Hair" ; "Natural Hair Building Fibers" "28g" or "Net Weight 28g"
Nice to have
- Make it stand out from the competition or similar to the brantiq example.

```html
<!DOCTYPE html>
<html lang="en">
<head>
<meta charset="utf-8">
<title>Velthar Pro – Hair Building Fibers Packaging Fronts</title>
<link rel="stylesheet" href="https://fonts.googleapis.com/css2?family=Inter:wght@300;700&family=Josefin+Sans:wght@300&family=Oswald:wght@200;300&display=swap">
<style>
  :root {
    --backdrop: #e4e4e4;
    --box-black: #121212;
    --label-white: #f1f1f1;
    --ink-dark: #1c1c1c;
    --text-light: #f4f4f4;
    --accent-her: #a83fb0;
    --accent-him: #2a6b64;
    --rule-light: #e9e9e9;
  }
  * { margin: 0; padding: 0; box-sizing: border-box; }
  html, body {
    width: 1200px;
    height: 1166px;
    overflow: hidden;
    background: var(--backdrop);
  }
  .canvas {
    position: relative;
    width: 1200px;
    height: 1166px;
  }
  .box-front {
    position: absolute;
    top: 158px;
    width: 400px;
    height: 850px;
    background: var(--box-black);
    font-family: "Inter", Arial, sans-serif;
  }
  .box-front--her { left: 170px; --accent: var(--accent-her); }
  .box-front--him { left: 630px; --accent: var(--accent-him); }

  .headline-band {
    position: absolute;
    top: 30px;
    left: 0;
    width: 100%;
    height: 150px;
    background: var(--label-white);
  }
  .headline {
    position: absolute;
    left: 22px;
    top: 26px;
    color: var(--ink-dark);
    line-height: 1.05;
  }
  .headline__light {
    display: block;
    font-weight: 300;
    font-size: 40px;
    letter-spacing: -0.5px;
  }
  .headline__bold {
    display: block;
    font-weight: 700;
    font-size: 40px;
    letter-spacing: -0.5px;
  }
  .headline__amp {
    position: absolute;
    right: 14px;
    top: 8px;
    font-family: "Josefin Sans", sans-serif;
    font-weight: 300;
    font-size: 112px;
    line-height: 1;
    color: var(--ink-dark);
  }
  .audience-tag {
    position: absolute;
    top: 160px;
    left: 118px;
    padding: 6px 12px 4px;
    border: 2px solid var(--ink-dark);
    background: var(--label-white);
    color: var(--accent);
    font-weight: 300;
    font-size: 19px;
    letter-spacing: 0.5px;
  }
  .brand-mark {
    position: absolute;
    top: 290px;
    left: 95px;
    width: 210px;
    height: 210px;
    border-radius: 50%;
    background: var(--label-white);
    display: flex;
    align-items: center;
    justify-content: center;
    color: var(--ink-dark);
    font-family: "Josefin Sans", sans-serif;
    font-weight: 300;
    font-size: 34px;
    letter-spacing: 3px;
    text-transform: lowercase;
  }
  .brand-name {
    position: absolute;
    top: 555px;
    left: 0;
    width: 100%;
    text-align: center;
    color: var(--text-light);
    font-family: "Josefin Sans", sans-serif;
    font-weight: 300;
    font-size: 31px;
    letter-spacing: 0.5em;
    text-indent: 0.5em;
  }
  .product-bar {
    position: absolute;
    top: 605px;
    left: 22px;
    width: 310px;
    height: 42px;
    background: var(--accent);
    color: var(--text-light);
    font-weight: 300;
    font-size: 20px;
    line-height: 42px;
    text-align: center;
  }
  .net-weight {
    position: absolute;
    top: 705px;
    left: 142px;
    width: 116px;
    height: 112px;
    border: 2px solid var(--rule-light);
    border-radius: 16px;
    color: var(--text-light);
    font-family: "Oswald", sans-serif;
    text-align: center;
  }
  .net-weight__label {
    display: block;
    margin-top: 14px;
    font-weight: 300;
    font-size: 17px;
    letter-spacing: 0.5px;
  }
  .net-weight__value {
    display: block;
    font-weight: 200;
    font-size: 46px;
    line-height: 1.1;
    letter-spacing: 2px;
  }
</style>
</head>
<body>
<main class="canvas">

  <section class="box-front box-front--her" aria-label="Packaging front for her">
    <div class="headline-band">
      <h1 class="headline">
        <span class="headline__light">Instant Fuller</span>
        <span class="headline__bold">Thicker Hair</span>
      </h1>
      <span class="headline__amp">&amp;</span>
    </div>
    <div class="audience-tag">FOR HER</div>
    <div class="brand-mark">velthar</div>
    <p class="brand-name">VELTHAR PRO</p>
    <p class="product-bar">Natural Hair Building Fibers</p>
    <div class="net-weight">
      <span class="net-weight__label">NET WEIGHT</span>
      <span class="net-weight__value">28G</span>
    </div>
  </section>

  <section class="box-front box-front--him" aria-label="Packaging front for him">
    <div class="headline-band">
      <h1 class="headline">
        <span class="headline__light">Instant Fuller</span>
        <span class="headline__bold">Thicker Hair</span>
      </h1>
      <span class="headline__amp">&amp;</span>
    </div>
    <div class="audience-tag">FOR HIM</div>
    <div class="brand-mark">velthar</div>
    <p class="brand-name">VELTHAR PRO</p>
    <p class="product-bar">Natural Hair Building Fibers</p>
    <div class="net-weight">
      <span class="net-weight__label">NET WEIGHT</span>
      <span class="net-weight__value">28G</span>
    </div>
  </section>

</main>
</body>
</html>
```